Visitenkarten für Elektro- und Informationstechnik-Betrieb
Zielgruppe
Wir sind ein Elektro- und Informationstechnik-Betrieb.
Unsere Fachgebiete sind Photovoltaikanlagen, Stromspeicher, Smart-Home und Ladestationrn
Aufgabenstellung
Design in der Farben des Logos und ein dunkler Hintergrund.

```html
<!DOCTYPE html>
<html lang="de">
<head>
<meta charset="utf-8">
<title>Visitenkarten – Elektro- und Informationstechnik Varnholt</title>
<link rel="stylesheet" href="https://fonts.googleapis.com/css2?family=Exo+2:wght@400;600;700&display=swap">
<style>
  :root {
    --stage: #e9eaee;
    --navy-light: #2b3b45;
    --navy-dark: #0f1c25;
    --copper: #c8794a;
    --steel-blue: #5f87a6;
    --paper: #ffffff;
    --ink-light: #f2f4f6;
  }
  * { box-sizing: border-box; margin: 0; padding: 0; }
  html, body { width: 1200px; height: 1200px; overflow: hidden; }
  body {
    background: var(--stage);
    font-family: "Exo 2", sans-serif;
    display: flex;
    flex-direction: column;
    align-items: center;
    justify-content: center;
    gap: 60px;
  }
  .card {
    width: 760px;
    height: 492px;
    position: relative;
    overflow: hidden;
    box-shadow: 0 18px 40px rgba(0,0,0,0.18);
  }
  .card--front {
    background: linear-gradient(30deg, var(--navy-dark) 0%, var(--navy-light) 100%);
    display: flex;
    align-items: center;
    justify-content: center;
  }
  .brand {
    display: flex;
    flex-direction: column;
    align-items: flex-start;
  }
  .brand__tagline {
    color: var(--steel-blue);
    font-weight: 400;
    font-size: 26px;
    letter-spacing: 0.5px;
  }
  .brand__name {
    display: flex;
    align-items: center;
    gap: 16px;
    color: var(--copper);
    font-weight: 700;
    font-size: 88px;
    line-height: 1;
    letter-spacing: 6px;
    text-transform: uppercase;
  }
  .brand__mark {
    width: 26px;
    height: 26px;
    background: var(--copper);
  }
  .card--back {
    background: linear-gradient(30deg, var(--navy-dark) 0%, var(--navy-light) 100%);
  }
  .back__band {
    position: absolute;
    left: 0; top: 0;
    width: 100%;
    height: 188px;
    background: var(--paper);
    display: flex;
    align-items: center;
    justify-content: center;
  }
  .back__band .brand__tagline { font-size: 18px; }
  .back__band .brand__name { font-size: 60px; letter-spacing: 4px; gap: 12px; }
  .back__band .brand__mark { width: 18px; height: 18px; }
  .person {
    position: absolute;
    left: 52px;
    top: 246px;
  }
  .person__name {
    color: var(--steel-blue);
    font-weight: 700;
    font-size: 26px;
  }
  .person__role {
    color: var(--ink-light);
    font-size: 19px;
    margin-top: 2px;
  }
  .contact {
    position: absolute;
    left: 380px;
    top: 222px;
    color: var(--ink-light);
    font-size: 18px;
    line-height: 1.4;
    list-style: none;
  }
  .contact__item {
    display: flex;
    gap: 16px;
    align-items: flex-start;
  }
  .contact__item + .contact__item { margin-top: 4px; }
  .contact__item--address { margin-bottom: 14px; }
  .contact__icon {
    width: 18px;
    height: 18px;
    flex: none;
    margin-top: 4px;
    fill: var(--ink-light);
  }
</style>
</head>
<body>
  <section class="card card--front" aria-label="Vorderseite">
    <div class="brand">
      <span class="brand__tagline">Elektro- und Informationstechnik</span>
      <span class="brand__name"><span class="brand__mark"></span>Varnholt</span>
    </div>
  </section>

  <section class="card card--back" aria-label="Rückseite">
    <div class="back__band">
      <div class="brand">
        <span class="brand__tagline">Elektro- und Informationstechnik</span>
        <span class="brand__name"><span class="brand__mark"></span>Varnholt</span>
      </div>
    </div>

    <div class="person">
      <p class="person__name">Timo Varnholt</p>
      <p class="person__role">Geschäftsführer</p>
    </div>

    <ul class="contact">
      <li class="contact__item contact__item--address">
        <svg class="contact__icon" viewBox="0 0 24 24"><path d="M12 3 2 12h3v9h5v-6h4v6h5v-9h3z"/></svg>
        <span>Elektro- und<br>Informationstechnik Varnholt<br>Am Lindenhang 7<br>54318 Musterau</span>
      </li>
      <li class="contact__item">
        <svg class="contact__icon" viewBox="0 0 24 24"><path d="M6.6 10.8a15 15 0 0 0 6.6 6.6l2.2-2.2a1 1 0 0 1 1-.25 11.4 11.4 0 0 0 3.6.57 1 1 0 0 1 1 1V20a1 1 0 0 1-1 1A17 17 0 0 1 3 4a1 1 0 0 1 1-1h3.5a1 1 0 0 1 1 1c0 1.25.2 2.45.57 3.57a1 1 0 0 1-.25 1z"/></svg>
        <span>+49 157 30418826</span>
      </li>
      <li class="contact__item">
        <svg class="contact__icon" viewBox="0 0 24 24"><path d="M2 5h20v14H2zm2 2v.5l8 5 8-5V7zm0 2.9V17h16V9.9l-8 5z"/></svg>
        <span>service@elektro-varnholt.example</span>
      </li>
      <li class="contact__item">
        <svg class="contact__icon" viewBox="0 0 24 24"><path d="M12 2a10 10 0 1 0 0 20 10 10 0 0 0 0-20zm6.9 6h-3a15 15 0 0 0-1.3-4A8 8 0 0 1 18.9 8zM12 4c.8 1.1 1.5 2.5 1.9 4h-3.8c.4-1.5 1.1-2.9 1.9-4zM4.3 14a8 8 0 0 1 0-4h3.4a16 16 0 0 0 0 4zm.8 2h3a15 15 0 0 0 1.3 4A8 8 0 0 1 5.1 16zm3-8h-3a8 8 0 0 1 4.3-4 15 15 0 0 0-1.3 4zM12 20c-.8-1.1-1.5-2.5-1.9-4h3.8c-.4 1.5-1.1 2.9-1.9 4zm2.3-6H9.7a14 14 0 0 1 0-4h4.6a14 14 0 0 1 0 4zm.3 6a15 15 0 0 0 1.3-4h3a8 8 0 0 1-4.3 4zm1.7-6a16 16 0 0 0 0-4h3.4a8 8 0 0 1 0 4z"/></svg>
        <span>www.elektro-varnholt.example</span>
      </li>
    </ul>
  </section>
</body>
</html>
```